Detailing informational flyer

I want to design a new flyer for my automotive detailing business. The flyer should use the color scheme from the logo and be easy to read and understand the services we offer.

Font styles to use
Serif
Sans Serif

Colors
3176b5
0255a3
fbed22
33a6d7
0692cd
ffffff

Requirements
Must have
• must include all information from the copy
Nice to have
• include a Glenvaro logo such as the image attached

```html
<!DOCTYPE html>
<html lang="en">
<head>
<meta charset="utf-8">
<title>Brookview Carwash Detailing Center – Flyer</title>
<link href="https://fonts.googleapis.com/css2?family=Poppins:wght@400;500;600;700&display=swap" rel="stylesheet">
<style>
  :root{
    --blue-mid:#3176b5;
    --blue-deep:#0255a3;
    --blue-body:#0c5fbf;
    --blue-dark:#0b4688;
    --blue-sky:#33a6d7;
    --blue-cyan:#0692cd;
    --blue-light:#5b9ae0;
    --yellow:#fbed22;
    --yellow-soft:#f3dc6a;
    --white:#ffffff;
    --paper:#e9e9eb;
    --text:#1d1d1d;
  }
  *{box-sizing:border-box;margin:0;padding:0}
  html,body{width:1200px;height:1000px;overflow:hidden}
  body{background:var(--paper);font-family:"Poppins",sans-serif;display:flex;align-items:center;justify-content:center}
  .flyer{position:relative;width:742px;height:960px;background:var(--blue-body);overflow:hidden;box-shadow:0 4px 14px rgba(0,0,0,.18)}
  .hero-photo{position:absolute;left:0;top:0;width:742px;height:340px;
    background:linear-gradient(120deg,#dfe8ec 0%,#b9c9d2 30%,#4f6f9c 52%,#2a3a4c 70%,#14181e 100%)}
  .hero-wave{position:absolute;left:0;top:250px;width:742px;height:140px}
  .logo-box{position:absolute;left:32px;top:24px;width:170px;height:134px;background:var(--blue-mid);
    border-radius:6px;display:flex;flex-direction:column;align-items:center;justify-content:center;gap:10px;padding:0 10px}
  .logo-dot{width:34px;height:34px;border-radius:50%;background:var(--yellow)}
  .logo-name{color:var(--yellow);font-weight:700;font-size:14px;line-height:1.3;letter-spacing:.5px;text-transform:uppercase;text-align:center}
  .title{position:absolute;left:0;right:0;top:368px;text-align:center;color:var(--white);font-weight:700;font-size:36px;letter-spacing:-.3px}
  .services{position:absolute;left:30px;right:30px;top:440px;display:flex;gap:12px}
  .service{flex:1;display:flex;flex-direction:column}
  .service-head{background:var(--blue-dark);color:var(--white);font-weight:600;font-size:15px;padding:8px 12px}
  .service-head.is-accent{background:var(--blue-light)}
  .service-body{background:var(--white);margin:0 2px;padding:12px 10px;font-size:10.5px;line-height:1.42;color:var(--text);height:222px}
  .mini{position:absolute;left:30px;right:30px;top:724px;border:2px solid var(--white);padding:16px 14px 10px;color:var(--white);font-size:10.8px;line-height:1.45}
  .mini-title{position:absolute;top:-12px;left:50%;transform:translateX(-50%);background:var(--blue-body);padding:0 12px;font-weight:600;font-size:15px;white-space:nowrap;line-height:22px}
  .footer{position:absolute;left:0;right:0;bottom:0;height:96px;background:var(--blue-dark);color:var(--white);
    display:flex;justify-content:space-between;align-items:center;padding:0 26px}
  .book h3{font-weight:700;font-size:15px}
  .book p{font-size:11px;line-height:1.4}
  .contact{text-align:right}
  .phones{display:flex;align-items:center;justify-content:flex-end;gap:8px;font-weight:500;font-size:15px;line-height:1.2;letter-spacing:1px}
  .address{font-size:11px;margin-top:8px}
</style>
</head>
<body>
  <article class="flyer">
    <div class="hero-photo" role="img" aria-label="Photo of a detailer in a blue shirt wiping a car dashboard with a green cloth"></div>
    <svg class="hero-wave" viewBox="0 0 742 140" preserveAspectRatio="none" aria-hidden="true">
      <path d="M0 70 C160 20 300 90 460 70 C580 55 680 40 742 30 L742 140 L0 140Z" fill="var(--blue-light)"/>
      <path d="M0 80 C160 30 300 100 460 82 C580 68 680 52 742 44 L742 140 L0 140Z" fill="var(--yellow-soft)"/>
      <path d="M0 98 C160 50 300 118 460 100 C580 88 680 72 742 64 L742 140 L0 140Z" fill="var(--blue-body)"/>
    </svg>

    <div class="logo-box">
      <span class="logo-dot"></span>
      <span class="logo-name">Brookview Carwash</span>
    </div>

    <h1 class="title">Brookview Carwash Detailing Center</h1>

    <section class="services">
      <div class="service">
        <h2 class="service-head">Exterior Detailing</h2>
        <p class="service-body">We wash, clay, compound, polish, and wax as needed to restore the deep rich gloss and provide a durable shine for that “new car” look. This process removes light oxidation from the vehicle and protects the clear coat finish. Finishing touches include rim cleaning and tire shine.</p>
      </div>
      <div class="service">
        <h2 class="service-head is-accent">Interior Detailing</h2>
        <p class="service-body">We perform a deep cleaning of the interior such as the dashboard, door jams, center console, trunk area, upholstered seats, and all carpets and mats. This process will remove soils and most stains. Windows are cleaned inside and out. All leather is dressed to provide a protective finish. Air freshener is available upon request.</p>
      </div>
      <div class="service">
        <h2 class="service-head">Headlight Restoration</h2>
        <p class="service-body">This shop proudly offers the Headlight Service, which can polish or restore your headlight to a clear, safe condition at a fraction of the cost of headlight replacement!<br>Restore the lens to a clear, shiny &amp; safe condition.</p>
      </div>
    </section>

    <section class="mini">
      <h2 class="mini-title">Mini Detail / VIP Service</h2>
      <p>Brookview Special Wash with triple polish wax, Glenvaro Shield protectant, tire shine, and a detailed and gentle cleaning of the upholstery. 4 rubber or carpet mats are shampooed. All interior surfaces are dressed including dashboard, door panels, center console. This is followed by a detailed carpet and upholstery vacuum with compressed air to remove dirt from hard to reach places. For added shine ask about adding on our express wax service to your mini detail package.</p>
    </section>

    <footer class="footer">
      <div class="book">
        <h3>BOOK TODAY</h3>
        <p>Ask to speak to a manager about<br>scheduling any of our detailing services.</p>
      </div>
      <div class="contact">
        <div class="phones">
          <svg width="24" height="24" viewBox="0 0 24 24" aria-hidden="true">
            <circle cx="12" cy="12" r="11" fill="none" stroke="var(--white)" stroke-width="1.6"/>
            <path d="M8.2 6.5l2 2.2-1 1.4c.8 1.6 2 2.8 3.6 3.6l1.4-1 2.2 2-1.2 1.9c-3.6-.3-7.2-3.9-7.5-7.5z" fill="var(--white)"/>
          </svg>
          <span>(555) 240-5400<br>(555) 240-5522</span>
        </div>
        <p class="address">88-20 Linden Ave. Corner Brookview Ave.</p>
      </div>
    </footer>
  </article>
</body>
</html>
```